Banner 34"x81"

This is for a Pull Up Banner
I am supplying a sample of my logo and some of my art work for you to incorporate into an upright banner.
Please business name:LuellaRo OpenHarbor Psychotherapy
phone number: 583-214-9067 NOT THE ONE ON THE BUSINESS CARD

```html
<!DOCTYPE html>
<html lang="en">
<head>
<meta charset="utf-8">
<title>LuellaRo OpenHarbor Psychotherapy – Pull Up Banner</title>
<link rel="stylesheet" href="https://fonts.googleapis.com/css2?family=Bebas+Neue&family=Montserrat:wght@700;800&family=Poppins:wght@500;600&display=swap">
<style>
  :root{
    --brand-blue:#2d59a8;
    --brand-red:#d0141c;
    --gold-light:#f3d57a;
    --gold-dark:#b8901f;
    --ink:#111111;
    --paper:#fbfbfd;
    --photo-top:#e9ecf3;
    --photo-mid:#2f5fd0;
    --photo-low:#6f7684;
  }
  *{margin:0;padding:0;box-sizing:border-box}
  html,body{width:1200px;height:3200px;overflow:hidden;background:var(--paper)}
  .banner{position:relative;width:1200px;height:3200px;background:var(--paper);overflow:hidden}
  .header-band{position:absolute;left:0;top:0;width:1200px;height:380px;background:var(--brand-blue);
    display:flex;align-items:center;justify-content:center}
  .logo-name{font-family:'Montserrat',sans-serif;font-weight:800;font-size:110px;color:#ffffff;letter-spacing:2px}
  .name-pill{position:absolute;left:320px;top:440px;width:560px;height:86px;border-radius:10px;
    background:linear-gradient(90deg,var(--gold-dark),var(--gold-light) 50%,var(--gold-dark));
    display:flex;align-items:center;justify-content:center;
    font-family:'Montserrat',sans-serif;font-weight:800;font-size:64px;letter-spacing:6px;color:var(--ink)}
  .practice-name{position:absolute;left:0;top:535px;width:1200px;text-align:center;
    font-family:'Bebas Neue',sans-serif;font-size:200px;line-height:1;color:var(--brand-blue)}
  .practice-type{position:absolute;left:0;top:735px;width:1200px;text-align:center;
    font-family:'Montserrat',sans-serif;font-weight:700;font-size:64px;letter-spacing:16px;color:var(--ink)}
  .photo{position:absolute;left:292px;top:930px;width:616px;height:1470px;
    background:linear-gradient(180deg,var(--photo-top) 0%,var(--photo-top) 30%,var(--photo-mid) 45%,var(--photo-mid) 65%,var(--photo-low) 80%,var(--photo-low) 100%)}
  .frame{position:absolute;left:0;top:0}
  .phone-pill{position:absolute;left:260px;top:2500px;width:680px;height:96px;background:var(--brand-red);
    border-radius:12px;display:flex;align-items:center}
  .phone-icon{position:absolute;left:-8px;top:-6px;width:108px;height:108px;border-radius:50%;
    background:radial-gradient(circle at 35% 35%,var(--gold-light),var(--gold-dark))}
  .phone-number{margin-left:120px;font-family:'Montserrat',sans-serif;font-weight:800;font-size:76px;color:#ffffff;letter-spacing:2px}
  .pill-shadow{position:absolute;left:200px;top:2610px;width:800px;height:40px;border-radius:50%;
    background:radial-gradient(ellipse at center,rgba(0,0,0,.18),rgba(0,0,0,0) 70%)}
  .mail-icon{position:absolute;left:565px;top:2670px;width:70px;height:70px;border-radius:50%;
    background:radial-gradient(circle at 35% 35%,var(--gold-light),var(--gold-dark))}
  .email{position:absolute;left:0;top:2760px;width:1200px;text-align:center;
    font-family:'Poppins',sans-serif;font-weight:600;font-size:46px;color:var(--ink)}
  .gold-rule{position:absolute;left:340px;top:2850px;width:520px;height:3px;
    background:linear-gradient(90deg,transparent,var(--gold-dark),transparent)}
  .socials{position:absolute;left:0;top:2900px;width:1200px;display:flex;justify-content:center;gap:40px;
    font-family:'Poppins',sans-serif;font-weight:600;font-size:40px;color:var(--ink)}
  .social{display:flex;align-items:center;gap:14px}
  .social-dot{width:34px;height:34px;border-radius:50%;background:var(--gold-dark)}
  .footer-band{position:absolute;left:0;top:3160px;width:1200px;height:40px;background:var(--brand-blue)}
</style>
</head>
<body>
<div class="banner">
  <header class="header-band"><span class="logo-name">LuellaRo</span></header>

  <div class="name-pill">LUELLA RO</div>
  <h1 class="practice-name">OPEN HARBOR</h1>
  <p class="practice-type">PSYCHOTHERAPY</p>

  <div class="photo" role="img" aria-label="Portrait photo of the therapist seated, smiling, wearing a blue top and grey plaid trousers"></div>
  <svg class="frame" width="1200" height="2440" viewBox="0 0 1200 2440" aria-hidden="true">
    <g fill="none" stroke="var(--brand-red)" stroke-width="12">
      <polyline points="276,2410 276,900 820,900"/>
      <polyline points="924,960 924,2410 276,2410"/>
    </g>
    <polygon points="850,880 890,900 850,920" fill="var(--brand-red)"/>
    <polygon points="900,880 940,900 900,920" fill="var(--brand-red)"/>
  </svg>

  <div class="phone-pill">
    <div class="phone-icon">
      <svg width="108" height="108" viewBox="0 0 108 108" aria-hidden="true">
        <path d="M36 30c4-3 8-2 10 2l6 11c2 3 1 6-2 8l-4 3c3 8 9 14 17 17l3-4c2-3 5-4 8-2l11 6c4 2 5 6 2 10l-4 5c-3 3-8 4-12 3-20-6-34-20-40-40-1-4 0-9 3-12z" fill="var(--brand-red)"/>
      </svg>
    </div>
    <span class="phone-number">583-214-9067</span>
  </div>
  <div class="pill-shadow"></div>

  <div class="mail-icon">
    <svg width="70" height="70" viewBox="0 0 70 70" aria-hidden="true">
      <rect x="17" y="22" width="36" height="26" fill="var(--brand-blue)"/>
      <polyline points="17,22 35,37 53,22" fill="none" stroke="#ffffff" stroke-width="3"/>
    </svg>
  </div>
  <p class="email">LuellaOpenHarbor@harbormail.com</p>
  <div class="gold-rule"></div>

  <div class="socials">
    <span class="social"><span class="social-dot"></span>@LuellaOpenHarbor</span>
    <span class="social"><span class="social-dot"></span>@LuellaHarbor</span>
  </div>

  <div class="footer-band"></div>
</div>
</body>
</html>
```